Arborist chip truck vehicle wrap / graphics

We need a wrap design for our chipper truck that we can tie other vehicles in with. We would like to see designs incorporating our logo colors in it and potentially some gold highlights.
Id like it to say Tree ROVER or tree surgeon somewhere.
a modern look is preferable
I would like the final design to be memorable and fairly simple.
Keep in mind this does not have to be a full truck wrap as we do like the white look. were looking for something interesting, use our logo as inspiration, we love it.
were highly trained and skilled and work on high end properties usually.

Target Market(s)

High end homeowners

Font styles to use
Other font styles liked:
• whatever my logo has on it

Requirements
Must have
• logo and name -
• the phrase tree Rover and /or tree surgeon
• some of our colors
• ceritifed arborist logo
• and member oke logo
Nice to have
• maybe something saying " Keeping your trees healthy and happy"
Should not have
• too busy
• there is no back gate so dont worry about the rear of the truck

```html
<!DOCTYPE html>
<html lang="en">
<head>
<meta charset="utf-8">
<title>FERN Tree Company – Vehicle Graphics</title>
<link rel="stylesheet" href="https://fonts.googleapis.com/css2?family=Archivo+Black&family=Questrial&display=swap">
<style>
  :root{
    --green:#1f8d3b;
    --green-faint:rgba(31,141,59,.14);
    --brown:#5b2a1f;
    --gold-deep:#e2b336;
    --gold-light:#f7e9b4;
    --white:#ffffff;
    --canvas:#eceeef;
    --edge:#cfd3d6;
    --badge:#3f7d2f;
    --badge-rim:#d9b648;
  }
  *{box-sizing:border-box;margin:0;padding:0}
  html,body{width:1200px;height:2424px;overflow:hidden;background:var(--canvas)}
  .sheet{position:relative;width:1200px;height:2424px}
  .panel{position:absolute;background:var(--white);border:1px solid var(--edge);border-radius:6px;overflow:hidden}
  .side-panel{left:60px;top:60px;width:1080px;height:540px}
  .hood-panel{left:240px;top:700px;width:720px;height:300px;border-radius:40px 40px 12px 12px}
  .rear-panel{left:170px;top:1110px;width:860px;height:1010px}
  .el{position:absolute}
  .badge{position:absolute;background:var(--badge);border:6px solid var(--badge-rim);border-radius:3px}
  .badge::after{content:"";position:absolute;left:18%;top:18%;width:64%;height:64%;border-radius:50%;background:var(--badge-rim);opacity:.55}
  .brand-dot{position:absolute;border-radius:50%;background:var(--green)}
  .brand-rule{position:absolute;width:3px;background:var(--brown)}
  .brand-name{position:absolute;font-family:"Questrial",sans-serif;color:var(--green);line-height:1}
  .brand-name .word{display:block}
  .slogan{position:absolute;font-family:"Archivo Black",sans-serif;color:var(--green);line-height:1.15;text-transform:uppercase}
  .role-tag{position:absolute;font-family:"Archivo Black",sans-serif;color:var(--brown);text-transform:uppercase}
  .contact-band{position:absolute;left:0;right:0;background:linear-gradient(90deg,var(--gold-deep) 0%,var(--gold-light) 45%,var(--gold-deep) 100%);display:flex;align-items:center;font-family:"Questrial",sans-serif;color:var(--white);letter-spacing:.14em;font-weight:700}
  .contact-band .divider{width:2px;align-self:stretch;margin:10px 0;background:var(--white)}
  .faint-disc{position:absolute;border-radius:50%;background:var(--green-faint)}
</style>
</head>
<body>
<main class="sheet">

  <!-- Box body, side -->
  <section class="panel side-panel" aria-label="Box body side graphics">
    <div class="faint-disc" style="left:860px;top:180px;width:280px;height:280px"></div>
    <div class="badge" style="left:24px;top:28px;width:78px;height:146px"></div>
    <div class="badge" style="left:966px;top:28px;width:84px;height:146px"></div>

    <div class="brand-dot" style="left:250px;top:100px;width:150px;height:150px"></div>
    <div class="brand-rule" style="left:448px;top:75px;height:175px"></div>
    <div class="brand-name" style="left:470px;top:96px">
      <span class="word" style="font-size:108px">FERN</span>
      <span class="word" style="font-size:32px;letter-spacing:.16em;margin-top:12px">TREE COMPANY</span>
    </div>

    <p class="slogan" style="left:54px;top:295px;font-size:34px">Keeping your trees<br>healthy and happy</p>
    <p class="role-tag" style="left:590px;top:333px;font-size:27px">Tree Surgeon</p>

    <div class="contact-band" style="top:412px;height:58px;font-size:31px">
      <span style="width:460px;text-align:center">555-010-4477</span>
      <span class="divider"></span>
      <span style="flex:1;text-align:center">WWW.FERNTREECOMPANY.COM</span>
    </div>
  </section>

  <!-- Cab front, hood -->
  <section class="panel hood-panel" aria-label="Cab hood graphics">
    <div class="brand-dot" style="left:120px;top:95px;width:120px;height:120px"></div>
    <div class="brand-rule" style="left:275px;top:70px;height:155px"></div>
    <div class="brand-name" style="left:295px;top:92px">
      <span class="word" style="font-size:92px">FERN</span>
      <span class="word" style="font-size:27px;letter-spacing:.16em;margin-top:10px">TREE COMPANY</span>
    </div>
  </section>

  <!-- Box body, rear -->
  <section class="panel rear-panel" aria-label="Box body rear graphics">
    <div class="badge" style="left:38px;top:25px;width:108px;height:178px"></div>
    <div class="badge" style="left:712px;top:25px;width:110px;height:178px"></div>

    <p class="role-tag" style="left:0;right:0;top:122px;text-align:center;font-size:42px">Tree Surgeon</p>

    <div class="brand-dot" style="left:100px;top:320px;width:200px;height:200px"></div>
    <div class="brand-rule" style="left:342px;top:290px;height:230px"></div>
    <div class="brand-name" style="left:362px;top:318px">
      <span class="word" style="font-size:128px">FERN</span>
      <span class="word" style="font-size:36px;letter-spacing:.16em;margin-top:14px">TREE COMPANY</span>
    </div>

    <p class="slogan" style="left:0;right:0;top:620px;text-align:center;font-size:52px">Keeping your trees<br>healthy and happy</p>

    <div class="contact-band" style="top:842px;height:64px;font-size:29px">
      <span style="width:265px;text-align:center">555-010-4477</span>
      <span class="divider"></span>
      <span style="flex:1;text-align:center">WWW.FERNTREECOMPANY.COM</span>
    </div>
  </section>

</main>
</body>
</html>
```